Ancient Art and Artifact information website

Hello Designers,
We are starting up a new website who talk abut and discusses an ancient arts artifacts. We would covering a wide range of countries ranging from Egypt, Greece, India, Syria, Rome, etc. My website name Tarn Wisp
Designs that fits with ancient theme and some kind of uniqueness would be accepted.
Requirements:
1) A home page design
2) Sub page design
3) A suitable logo
Sections can be added are featured ancient arts/places with short description followed by a more button, latest news, and comment section.
Add contents if you found relevant for this category of website. Ability to share the information through social media is desired.
Must be a responsive design. I look forward to designs which are mind blowing.
Number of Pages Required
2 page

```html
<!DOCTYPE html>
<html lang="en">
<head>
<meta charset="utf-8">
<title>Tarn Wisp — Ancient Art and Artifacts</title>
<link rel="stylesheet" href="https://fonts.googleapis.com/css2?family=Poppins:wght@300;400;500;600&family=Crimson+Text:ital@0;1&display=swap">
<style>
:root{
  --gold:#e2ac32;
  --ink:#1b1b1b;
  --text:#6f6f6f;
  --muted:#9a9a9a;
  --card:#efefef;
  --pill:#a3a3a3;
  --dark:#121212;
  --darker:#0a0a0a;
  --band:#f7f7f7;
  --line:#2a2a2a;
  --white:#ffffff;
}
*{margin:0;padding:0;box-sizing:border-box}
html,body{width:1200px;height:2946px;overflow:hidden;background:var(--white)}
body{font-family:"Poppins",sans-serif;color:var(--ink)}
.canvas{position:relative;width:1200px;height:2946px;overflow:hidden}
.abs{position:absolute}

/* top bar */
.topbar{left:0;top:0;width:1200px;height:52px}
.topbar-dark{position:absolute;left:240px;top:0;right:0;height:52px;background:var(--dark);clip-path:polygon(0 0,100% 0,100% 100%,34px 100%)}
.signin{left:328px;top:14px;color:var(--white);font-size:14px;display:flex;align-items:center;gap:16px}
.social-top{left:572px;top:0;display:flex;height:52px}
.social-top span{width:51px;height:52px;border-left:1px solid #333;display:flex;align-items:center;justify-content:center}
.social-top span:last-child{border-right:1px solid #333}
.social-top i{width:11px;height:11px;background:#777;display:block}
.social-top span.active i{background:var(--gold)}
.search-top{left:1050px;top:0;width:90px;height:52px;border-left:1px solid #333;display:flex;align-items:center;justify-content:center}

/* header */
.brand{display:flex;align-items:center;gap:10px;font-family:"Poppins",sans-serif;font-weight:500;font-size:26px;color:var(--gold);letter-spacing:-.5px}
.brand-mark{width:28px;height:28px;border-radius:50%;background:#8a5a38}
.header-brand{left:82px;top:50px}
.nav{left:533px;top:86px;display:flex;gap:0;font-size:13px;font-weight:500;color:var(--ink)}
.nav a{text-decoration:none;color:inherit;margin-right:38px}
.nav a.current{color:var(--gold)}
.nav .caret{font-size:9px;margin-left:8px;color:#888}

/* hero */
.hero{left:0;top:133px;width:1200px;height:392px;background:linear-gradient(180deg,#5a4a3a,#3b2e24 60%,#2c231c)}
.hero-title{left:116px;top:278px;font-size:47px;font-weight:300;line-height:68px;color:var(--white)}
.hero-thumb{position:absolute;border-radius:6px}
.hero-label{position:absolute;font-size:13px;color:var(--white);text-align:center;width:100px}
.hero-dots{left:578px;top:500px;display:flex;gap:10px}
.hero-dots i{width:7px;height:7px;border-radius:50%;background:#888;display:block}
.hero-dots i.on{background:#ddd}

/* welcome */
.eyebrow{font-size:19px;color:var(--gold);font-weight:300}
.section-title{font-size:31px;font-weight:600;color:var(--ink);letter-spacing:.5px}
.welcome-eyebrow{left:82px;top:570px}
.welcome-title{left:82px;top:598px}
.welcome-copy{left:82px;top:665px;width:585px;font-size:14.5px;line-height:25.5px;color:var(--text)}
.welcome-copy p+p{margin-top:27px}
.btn-outline{display:flex;align-items:center;justify-content:center;border:2px solid #222;border-radius:9px;font-size:15px;font-weight:600;color:var(--gold);letter-spacing:.5px}
.welcome-btn{left:82px;top:932px;width:158px;height:45px}
.welcome-img{left:712px;top:579px;width:406px;height:398px;background:linear-gradient(160deg,#d8d4cc,#a9a49b)}

/* artifacts */
.center-eyebrow{left:0;width:1200px;text-align:center}
.arrows{width:110px;height:45px;background:#2a2a2a;display:flex;align-items:center;justify-content:space-around}
.arrows b{width:1px;height:16px;background:#555}
.card{position:absolute;width:310px;height:426px;background:var(--card);border-radius:6px;overflow:hidden}
.card-img{height:224px}
.card-body{padding:20px 18px 0 18px}
.card-title{font-size:14.5px;line-height:24px;color:#222;height:54px}
.card-text{font-size:13px;line-height:22px;color:var(--muted);margin-top:5px}
.card-foot{position:absolute;left:18px;right:18px;bottom:26px;display:flex;align-items:center;justify-content:space-between}
.pill{background:var(--pill);color:var(--white);font-size:11px;font-weight:600;padding:7px 13px;border-radius:5px}
.pill.gold{background:var(--gold)}
.comments{display:flex;align-items:center;gap:18px;font-size:12px;color:var(--muted)}

/* news */
.news-band{left:0;top:2062px;width:1200px;height:495px;background:var(--band)}
.news-img{left:82px;top:2195px;width:505px;height:310px;background:linear-gradient(150deg,#c7b595,#8e7a5c)}
.news-day{left:615px;top:2215px;font-size:62px;font-weight:300;color:#111;line-height:1}
.news-month{left:700px;top:2228px;font-family:"Poppins",sans-serif;font-size:17px;font-weight:300;font-style:italic;color:#777;line-height:24px}
.news-title{left:617px;top:2305px;font-size:14.5px;font-weight:500;color:#111}
.news-text{left:617px;top:2345px;width:500px;font-family:"Crimson Text",serif;font-size:13px;line-height:22px;color:var(--muted)}
.news-meta{left:617px;top:2410px;font-family:"Crimson Text",serif;font-size:13px;color:#444;display:flex;align-items:center;gap:14px}
.news-btn{left:615px;top:2457px;width:158px;height:45px}

/* footer */
.footer{left:0;top:2557px;width:1200px;height:389px;background:var(--dark)}
.footer-brand{left:82px;top:2603px}
.footer-about{left:82px;top:2668px;width:330px;font-family:"Crimson Text",serif;font-size:13.5px;line-height:23px;color:#ccc}
.footer-social{left:82px;top:2760px;display:flex;gap:14px}
.footer-social span{width:32px;height:32px;border-radius:50%;border:1px solid #444;display:flex;align-items:center;justify-content:center}
.footer-social i{width:9px;height:9px;background:#ddd;display:block}
.footer-heading{font-size:13.5px;font-weight:600;color:var(--white);letter-spacing:.5px}
.footer-info-title{left:537px;top:2628px}
.footer-links{left:537px;top:2670px;list-style:none;font-size:12px;font-weight:500;color:var(--white);line-height:29px}
.footer-links li.current{color:var(--gold)}
.footer-news-title{left:880px;top:2628px}
.email{left:880px;top:2707px;width:240px;height:39px;background:var(--darker);font-family:"Crimson Text",serif;font-style:italic;font-size:12px;color:#888;padding:11px 24px}
.subscribe{left:880px;top:2759px;width:240px;height:38px;background:var(--gold);font-size:11px;font-weight:600;color:#111;display:flex;align-items:center;justify-content:center;letter-spacing:.5px}
.footer-rule{left:0;top:2888px;width:1200px;height:1px;background:var(--line)}
.copyright{left:0;top:2908px;width:1200px;text-align:center;font-family:"Crimson Text",serif;font-size:12px;color:#999}
</style>
</head>
<body>
<div class="canvas">

  <!-- top bar -->
  <div class="abs topbar"><div class="topbar-dark"></div></div>
  <div class="abs signin">
    <svg width="18" height="18" viewBox="0 0 18 18"><circle cx="9" cy="9" r="8.5" fill="#fff"/><circle cx="9" cy="7" r="3" fill="#121212"/><path d="M3.5 14.5c1.2-2.6 3.2-3.6 5.5-3.6s4.3 1 5.5 3.6" fill="#121212"/></svg>
    <span>Sign in</span>
  </div>
  <div class="abs social-top">
    <span class="active"><i></i></span><span><i></i></span><span><i></i></span><span><i></i></span>
  </div>
  <div class="abs search-top">
    <svg width="18" height="18" viewBox="0 0 18 18"><circle cx="7.5" cy="7.5" r="5.5" fill="none" stroke="#fff" stroke-width="2"/><path d="M11.5 11.5l5 5" stroke="#fff" stroke-width="2"/></svg>
  </div>

  <!-- header -->
  <div class="abs brand header-brand"><span class="brand-mark"></span>Tarn Wisp</div>
  <nav class="abs nav">
    <a class="current">HOME</a><a>ABOUT US</a><a>ANCIENT ART ARTIFACTS<span class="caret">&#9660;</span></a><a>GALLERY</a><a>LATEST NEWS</a>
  </nav>

  <!-- hero -->
  <div class="abs hero" role="img" aria-label="Carved temple wall relief in dark stone, backdrop of the hero slider"></div>
  <h1 class="abs hero-title">Lorem ipsum dolor sit<br>amet consect</h1>
  <div class="hero-thumb abs" style="left:810px;top:166px;width:90px;height:140px;background:linear-gradient(160deg,#e2d6bc,#b9a985)" role="img" aria-label="Syrian stone relief artifact"></div>
  <div class="hero-label" style="left:828px;top:313px">Syria</div>
  <div class="hero-thumb abs" style="left:1020px;top:178px;width:86px;height:138px;background:linear-gradient(160deg,#d8d2c4,#9d9484)" role="img" aria-label="Indian carved deity statue"></div>
  <div class="hero-label" style="left:1020px;top:327px">India</div>
  <div class="hero-thumb abs" style="left:650px;top:328px;width:168px;height:116px;background:linear-gradient(160deg,#d7c39a,#a98a5c)" role="img" aria-label="Egyptian painted wall fragment"></div>
  <div class="hero-label" style="left:682px;top:457px">Egypt</div>
  <div class="hero-thumb abs" style="left:940px;top:340px;width:84px;height:120px;border-radius:40px 40px 20px 20px;background:linear-gradient(160deg,#c9722e,#6b3414)" role="img" aria-label="Greek painted amphora"></div>
  <div class="hero-label" style="left:936px;top:462px">Greece</div>
  <div class="abs hero-dots"><i></i><i></i><i class="on"></i></div>

  <!-- welcome -->
  <div class="abs eyebrow welcome-eyebrow">Welcome to</div>
  <h2 class="abs section-title welcome-title">TARN WISP</h2>
  <div class="abs welcome-copy">
    <p>Lorem ipsum dolor sit amet, consectetur adipiscing elit. Nunc sollicitudin ex id feugiat varius. Cras tincidunt diam vel ex lacinia placerat. Mauris ultrices vulputate felis, eget convallis mi mattis ullamcorper. Mauris vehicula libero ac sagittis euismod. Nullam bibendum congue placerat. Fusce ornare scelerisque leo,</p>
    <p>Cras tincidunt diam vel ex lacinia placerat. Mauris ultrices vulputate felis, eget convallis mi mattis ullamcorper. Mauris vehicula libero ac sagittis euismod. Nullam bibendum congue placerat.</p>
  </div>
  <div class="abs btn-outline welcome-btn">READ MORE</div>
  <div class="abs welcome-img" role="img" aria-label="Marble relief of a seated mother with children"></div>

  <!-- artifacts -->
  <div class="abs eyebrow center-eyebrow" style="top:1027px">Ancient</div>
  <h2 class="abs section-title center-eyebrow" style="top:1053px">AN ANCIENT ARTS ARTIFACTS</h2>
  <div class="abs arrows" style="left:1008px;top:1037px">
    <svg width="8" height="10" viewBox="0 0 8 10"><path d="M7 1L1 5l6 4z" fill="none" stroke="#e2ac32" stroke-width="1.4"/></svg><b></b>
    <svg width="8" height="10" viewBox="0 0 8 10"><path d="M1 1l6 4-6 4z" fill="none" stroke="#e2ac32" stroke-width="1.4"/></svg>
  </div>

  <article class="card" style="left:82px;top:1121px">
    <div class="card-img" role="img" aria-label="Hittite carved statue base with lion figures" style="background:linear-gradient(160deg,#cfcfcf,#7d7d7d)"></div>
    <div class="card-body"><div class="card-title">Hittite, base of a statue,(King's Gate) Karkamış,</div>
    <div class="card-text">Lorem ipsum dolor sit amet, consect etur adipiscing elit. Nunc sollicitudin ex id feugiat varius. Cras tincidunt diam</div></div>
    <div class="card-foot"><span class="pill gold">READ MORE</span><span class="comments"><svg width="16" height="14" viewBox="0 0 16 14"><path d="M1 1h14v9H6l-4 3v-3H1z" fill="#555"/></svg>17 comments</span></div>
  </article>
  <article class="card" style="left:455px;top:1121px">
    <div class="card-img" role="img" aria-label="Blue cameo glass vase" style="background:linear-gradient(160deg,#9fb0c4,#2f4f86)"></div>
    <div class="card-body"><div class="card-title">The blue vase from Pompeii. Naples</div>
    <div class="card-text">Lorem ipsum dolor sit amet, consect etur adipiscing elit. Nunc sollicitudin ex id feugiat varius. Cras tincidunt diam</div></div>
    <div class="card-foot"><span class="pill">READ MORE</span><span class="comments"><svg width="16" height="14" viewBox="0 0 16 14"><path d="M1 1h14v9H6l-4 3v-3H1z" fill="#555"/></svg>17 comments</span></div>
  </article>
  <article class="card" style="left:808px;top:1121px">
    <div class="card-img" role="img" aria-label="Gold Roman fibula brooch with cameo" style="background:radial-gradient(circle at 50% 50%,#d9a63a,#6a4a12 60%,#151515 85%)"></div>
    <div class="card-body"><div class="card-title">Large Royal Roman Fibula with Cameo</div>
    <div class="card-text">Lorem ipsum dolor sit amet, consect etur adipiscing elit. Nunc sollicitudin ex id feugiat varius. Cras tincidunt diam</div></div>
    <div class="card-foot"><span class="pill">READ MORE</span><span class="comments"><svg width="16" height="14" viewBox="0 0 16 14"><path d="M1 1h14v9H6l-4 3v-3H1z" fill="#555"/></svg>17 comments</span></div>
  </article>

  <article class="card" style="left:82px;top:1586px">
    <div class="card-img" role="img" aria-label="Blue enamelled Iranian lidded vessel" style="background:linear-gradient(180deg,#e6c93a,#2a3fa0 75%)"></div>
    <div class="card-body"><div class="card-title">Archeological excavations on the Iranian</div>
    <div class="card-text">Lorem ipsum dolor sit amet, consect etur adipiscing elit. Nunc sollicitudin ex id feugiat varius. Cras tincidunt diam</div></div>
    <div class="card-foot"><span class="pill">READ MORE</span><span class="comments"><svg width="16" height="14" viewBox="0 0 16 14"><path d="M1 1h14v9H6l-4 3v-3H1z" fill="#555"/></svg>17 comments</span></div>
  </article>
  <article class="card" style="left:455px;top:1586px">
    <div class="card-img" role="img" aria-label="Painted Greek neck amphora" style="background:linear-gradient(160deg,#c9c6c0,#6e3a22)"></div>
    <div class="card-body"><div class="card-title">Neck amphora (storage jar), ca. 620/615–595/590 b.c. Gree</div>
    <div class="card-text">Lorem ipsum dolor sit amet, consect etur adipiscing elit. Nunc sollicitudin ex id feugiat varius. Cras tincidunt diam</div></div>
    <div class="card-foot"><span class="pill">READ MORE</span><span class="comments"><svg width="16" height="14" viewBox="0 0 16 14"><path d="M1 1h14v9H6l-4 3v-3H1z" fill="#555"/></svg>17 comments</span></div>
  </article>
  <article class="card" style="left:808px;top:1586px">
    <div class="card-img" role="img" aria-label="Bronze amphora pitcher with sculpted handle" style="background:linear-gradient(160deg,#f2f0ec,#8a6f4e)"></div>
    <div class="card-body"><div class="card-title" style="padding-top:12px">Rare Amphora Pitcher</div>
    <div class="card-text">Lorem ipsum dolor sit amet, consect etur adipiscing elit. Nunc sollicitudin ex id feugiat varius. Cras tincidunt diam</div></div>
    <div class="card-foot"><span class="pill">READ MORE</span><span class="comments"><svg width="16" height="14" viewBox="0 0 16 14"><path d="M1 1h14v9H6l-4 3v-3H1z" fill="#555"/></svg>17 comments</span></div>
  </article>

  <!-- latest news -->
  <div class="abs news-band"></div>
  <div class="abs eyebrow" style="left:82px;top:2104px">What Our Client Says</div>
  <h2 class="abs section-title" style="left:82px;top:2130px">LATEST NEWS</h2>
  <div class="abs arrows" style="left:1008px;top:2112px">
    <svg width="8" height="10" viewBox="0 0 8 10"><path d="M7 1L1 5l6 4z" fill="none" stroke="#e2ac32" stroke-width="1.4"/></svg><b></b>
    <svg width="8" height="10" viewBox="0 0 8 10"><path d="M1 1l6 4-6 4z" fill="none" stroke="#e2ac32" stroke-width="1.4"/></svg>
  </div>
  <div class="abs news-img" role="img" aria-label="Carved marble sarcophagus frieze"></div>
  <div class="abs news-day">08</div>
  <div class="abs news-month">March<br>2017</div>
  <div class="abs news-title">LOREM IPSUM DOLOR SIT AMET CONSECTETUR ADIPISCING ELIT</div>
  <div class="abs news-text">Then one day he was shooting at some food and up through the ground came a crude oil that is so lets bubbling make the most of this beautiful day.</div>
  <div class="abs news-meta"><span>Orin Halvey</span>
    <svg width="14" height="12" viewBox="0 0 14 12"><path d="M1 1h12v7H5l-3 3V8H1z" fill="none" stroke="#e2ac32" stroke-width="1.2"/></svg><span>17 Comments</span></div>
  <div class="abs btn-outline news-btn">READ MORE</div>

  <!-- footer -->
  <footer class="abs footer"></footer>
  <div class="abs brand footer-brand"><span class="brand-mark"></span>Tarn Wisp</div>
  <p class="abs footer-about">Then one day he was shooting at some food and up the ground came a crude oil day he was shooting at some food.</p>
  <div class="abs footer-social"><span><i></i></span><span><i></i></span><span><i></i></span><span><i></i></span><span><i></i></span></div>
  <div class="abs footer-heading footer-info-title">INFORMATION</div>
  <ul class="abs footer-links">
    <li class="current">HOME</li><li>ABOUT US</li><li>ANCIENT ART ARTIFACTS</li><li>GALLERY</li><li>LATEST NEWS</li>
  </ul>
  <div class="abs footer-heading footer-news-title">NEWSLETTER</div>
  <div class="abs email">Your Email id</div>
  <div class="abs subscribe">SUBSCRIBE</div>
  <div class="abs footer-rule"></div>
  <div class="abs copyright">Copyrights © 2016. All Rights Reserved</div>

</div>
</body>
</html>
```